Title loan company needs a postcard design, front/back, for marketing to former customers

We need a clean postcard design for the purpose of a mailer to engage former customers to come in and take out a loan.
We want to reinforce the benefits of doing business with us and give them an incentive offer to borrow money with us again.

The special offer: $50 Bonus Cash on your next loan

Some points or benefits we offer:
-No Credit Check
-Instant Approval
-Easy Payments
-15 Minute Loans
-Maple Ledger Certified-I am providing this as a image for a state association we are members of. You may use the logo or use it as a benefit.
-Satisfaction Guarantee-I am providing this as an image as a guarantee. I personally feel that this should image should be used as a reinforcement of said guarantee.

The loan product is know as a title loan. The customer pledges the car title to their vehicle as security for the loan in exchange for cash.

Front and back of the card should have a call to action.
Looking for a clean design for the front and back of the postcard.
Back of the card should have a space for postage stamp, or indicia, and enough room for a mailing label

Visit our website for any additional information that you may have or ask me directly.

ridgelinegroup.com

Hex color codes of the logo should you incorporate this into the design.
Light Green in Logo: #b7dc78
Dark Green in Logo: #00953a
Yellow in Logo: #ffdd00

I am attaching our logo, the maple ledger seal, and the guarantee shield.
I am also attaching templates for illustrator, photoshop, acrobat. Use one of the templates as it has the correct bleeds for my printer. If you need another template let me know.

Reason: I am extending the deadline but I only really need a day before i choose the final design. Had a technical error that prevents me from getting this done & it should be rectified by the end of the day today?

25-54
Male/Female = 50% Split

Loan

Serif
Sans Serif

• Clean Design, Call to Action, Draw attention to special offer
• Use of some of the colors in logo, hex color codes are in description, for branding purposes! Not a requirement! Let see what you bring to the table.

```html
<!DOCTYPE html>
<html lang="en">
<head>
<meta charset="utf-8">
<title>Ridgeline Title Loans – Postcard Front and Back</title>
<link rel="stylesheet" href="https://fonts.googleapis.com/css2?family=Oswald:wght@400;500&family=Roboto:wght@300;400&family=Source+Sans+3:wght@400&display=swap">
<style>
  :root {
    --green-dark: #00953a;
    --green-light: #b7dc78;
    --green-mid: #8cc63f;
    --yellow: #ffdd00;
    --grey-band: #e6e7e6;
    --grey-text: #4a4a4a;
    --stamp: #e5e5e5;
    --white: #ffffff;
  }
  html, body {
    margin: 0;
    width: 1200px;
    height: 960px;
    overflow: hidden;
  }
  body {
    background: radial-gradient(ellipse at 50% 15%, #5a5a5a 0%, #3a3a3a 55%, #2f2f2f 100%);
    font-family: "Roboto", sans-serif;
    position: relative;
  }
  .card {
    position: absolute;
    top: 276px;
    width: 551px;
    height: 390px;
    background: var(--white);
    overflow: hidden;
    box-shadow: 0 6px 14px rgba(0,0,0,.45);
  }
  .card--front { left: 34px; }
  .card--back { left: 617px; }
  .side-label {
    position: absolute;
    top: 718px;
    font-family: "Source Sans 3", sans-serif;
    font-size: 56px;
    color: var(--white);
    line-height: 1;
  }
  .side-label--front { left: 264px; }
  .side-label--back { left: 816px; }

  /* front */
  .hero-photo {
    position: absolute;
    left: 0; top: 0;
    width: 300px; height: 390px;
    background:
      radial-gradient(ellipse at 30% 55%, #e9d3b0 0%, rgba(233,211,176,0) 45%),
      radial-gradient(ellipse at 65% 55%, #d9c7b4 0%, rgba(217,199,180,0) 40%),
      linear-gradient(160deg, #6c6f8f 0%, #b9bccd 30%, #f2f2f2 55%, #cfd8c4 80%, #f7f7f7 100%);
  }
  .curve { position: absolute; left: 0; top: 0; }
  .brand-name {
    position: absolute;
    left: 96px; top: 338px;
    font-family: "Roboto", sans-serif;
    font-weight: 400;
    font-size: 19px;
    color: #1a1a1a;
    display: flex; align-items: center; gap: 6px;
  }
  .brand-name .mark {
    width: 12px; height: 12px; border-radius: 50%;
    background: var(--green-dark);
  }
  .headline {
    position: absolute;
    font-family: "Oswald", sans-serif;
    font-weight: 500;
    text-transform: uppercase;
    letter-spacing: .3px;
    line-height: 27px;
    margin: 0;
  }
  .headline .light { color: var(--green-light); display: block; }
  .headline .dark { color: var(--green-dark); display: block; }
  .front-headline { left: 308px; top: 21px; font-size: 23px; text-align: center; width: 230px; }
  .offer-band {
    position: absolute;
    left: 270px; top: 92px;
    width: 281px; height: 68px;
    background: var(--grey-band);
  }
  .offer-amount {
    position: absolute;
    left: 300px; top: 92px;
    font-family: "Oswald", sans-serif;
    font-weight: 500;
    font-size: 54px;
    line-height: 68px;
    color: var(--green-dark);
  }
  .offer-text {
    position: absolute;
    left: 388px; top: 101px;
    color: var(--grey-text);
    line-height: 1;
  }
  .offer-text .big { font-size: 26px; display: block; }
  .offer-text .small { font-size: 19.5px; font-weight: 300; display: block; margin-top: 2px; }
  .offer-tab {
    position: absolute;
    left: 290px; top: 186px;
    width: 104px; height: 24px;
    background: var(--green-light);
    clip-path: polygon(0 0, 100% 0, 96% 100%, 0 100%);
    font-family: "Oswald", sans-serif;
    color: var(--white);
    font-size: 17px;
    line-height: 24px;
    padding-left: 16px;
    box-sizing: border-box;
  }
  .badge { position: absolute; top: 171px; }
  .benefits {
    position: absolute;
    left: 314px; top: 224px;
    display: grid;
    grid-template-columns: 110px 110px;
    row-gap: 9px;
    column-gap: 0;
    margin: 0; padding: 0; list-style: none;
    font-family: "Oswald", sans-serif;
    font-weight: 400;
    font-size: 12.5px;
    color: var(--grey-text);
  }
  .benefits li { display: flex; align-items: center; gap: 6px; height: 16px; }
  .benefit-icon {
    width: 20px; height: 13px;
    border: 1.5px solid var(--green-mid);
    border-radius: 3px;
    box-sizing: border-box;
    display: flex; align-items: center; justify-content: center;
  }
  .front-contact-title {
    position: absolute;
    right: 19px; top: 290px;
    font-family: "Oswald", sans-serif;
    font-weight: 500;
    font-size: 21px;
    color: var(--green-dark);
    margin: 0;
  }
  .front-contact-rule {
    position: absolute;
    left: 360px; top: 316px;
    width: 172px; height: 2px;
    background: var(--green-light);
  }
  .front-phone {
    position: absolute;
    right: 19px; top: 319px;
    font-size: 32px;
    font-weight: 300;
    color: var(--grey-text);
    letter-spacing: .5px;
  }
  .front-footer {
    position: absolute;
    left: 310px; top: 364px;
    width: 241px; height: 26px;
    background: var(--grey-band);
    font-size: 12.5px;
    line-height: 26px;
    color: #333;
    text-align: center;
  }
  .front-footer .accent { color: var(--green-dark); }

  /* back */
  .back-headline { left: 19px; top: 16px; font-size: 22px; line-height: 25px; }
  .about {
    position: absolute;
    left: 19px; top: 78px;
    width: 221px;
    margin: 0;
    font-size: 10.4px;
    line-height: 13.55px;
    color: var(--grey-text);
    text-align: justify;
    font-weight: 400;
  }
  .back-band {
    position: absolute;
    left: 0; top: 264px;
    width: 300px; height: 126px;
    background: var(--grey-band);
  }
  .back-contact-title {
    position: absolute;
    left: 21px; top: 272px;
    font-family: "Oswald", sans-serif;
    font-weight: 500;
    font-size: 21px;
    color: var(--green-dark);
    margin: 0;
  }
  .back-contact-rule {
    position: absolute;
    left: 21px; top: 299px;
    width: 183px; height: 2px;
    background: var(--green-light);
  }
  .contact-line {
    position: absolute;
    left: 23px;
    display: flex; align-items: center; gap: 10px;
    color: var(--grey-text);
  }
  .contact-line--phone { top: 309px; font-size: 18px; font-weight: 300; }
  .contact-line--web { top: 336px; font-size: 13px; }
  .social {
    position: absolute;
    left: 21px; top: 365px;
    display: flex; align-items: center; gap: 4px;
    font-size: 7px; color: var(--grey-text);
  }
  .social .lead { margin-right: 10px; }
  .social .dot {
    width: 17px; height: 17px; border-radius: 50%;
    background: var(--green-dark);
  }
  .stamp-box {
    position: absolute;
    left: 474px; top: 21px;
    width: 59px; height: 57px;
    background: var(--stamp);
  }
</style>
</head>
<body>

<section class="card card--front" aria-label="Postcard front">
  <div class="hero-photo" role="img" aria-label="Photo of a smiling couple in a convertible car on a sunny day"></div>

  <svg class="curve" width="551" height="390" viewBox="0 0 551 390" aria-hidden="true">
    <path d="M300 0 L551 0 L551 390 L282 390 C270 300 262 180 300 0 Z" fill="#ffffff"/>
    <path d="M299 0 L304 0 C284 110 281 250 305 390 L282 390 C262 270 270 120 299 0 Z" fill="#00953a"/>
    <path d="M291 0 L297 0 C268 120 266 260 286 390 L278 390 C256 260 262 120 291 0 Z" fill="#b7dc78"/>
  </svg>

  <div class="brand-name"><span class="mark"></span>Ridgeline Title Loans</div>

  <h1 class="headline front-headline">
    <span class="light">Drive away with the</span>
    <span class="dark">Cash you need today!</span>
  </h1>

  <div class="offer-band"></div>
  <div class="offer-amount">$50</div>
  <div class="offer-text"><span class="big">Bonus Cash</span><span class="small">on your next loan</span></div>

  <div class="offer-tab">WE OFFER</div>

  <svg class="badge" style="left:441px" width="40" height="40" viewBox="0 0 40 40" role="img" aria-label="Maple Ledger Certified seal">
    <circle cx="20" cy="20" r="19" fill="#00953a"/>
    <circle cx="20" cy="20" r="13" fill="#b7dc78"/>
  </svg>
  <svg class="badge" style="left:494px" width="34" height="40" viewBox="0 0 34 40" role="img" aria-label="Satisfaction guarantee shield">
    <path d="M17 1 L33 6 L33 20 C33 30 25 36 17 39 C9 36 1 30 1 20 L1 6 Z" fill="#00953a"/>
    <path d="M17 6 L28 9.5 L28 20 C28 27 22 31 17 33 C12 31 6 27 6 20 L6 9.5 Z" fill="#d9dcd6"/>
  </svg>

  <ul class="benefits">
    <li><span class="benefit-icon"><svg width="10" height="6" viewBox="0 0 10 6"><rect width="10" height="6" rx="1" fill="#ffdd00"/></svg></span>No Credit Check</li>
    <li><span class="benefit-icon"><svg width="9" height="7" viewBox="0 0 9 7"><path d="M1 4 L3.5 6.5 L8 1" stroke="#ffdd00" stroke-width="2" fill="none"/></svg></span>Instant Approval</li>
    <li><span class="benefit-icon"><svg width="8" height="8" viewBox="0 0 8 8"><rect x="1" y="0.5" width="6" height="7" rx="1" fill="#00953a"/></svg></span>Easy Payments</li>
    <li><span class="benefit-icon"><svg width="9" height="9" viewBox="0 0 9 9"><circle cx="4.5" cy="4.5" r="3.6" stroke="#ffdd00" stroke-width="1.2" fill="none"/><path d="M4.5 2.5 V4.7 H6" stroke="#00953a" stroke-width="1" fill="none"/></svg></span>15 Minute Loans</li>
  </ul>

  <h2 class="front-contact-title">CONTACT US</h2>
  <div class="front-contact-rule"></div>
  <div class="front-phone">123-456-789</div>

  <div class="front-footer">www.<span class="accent">ridgelinegroup</span>.com</div>
</section>

<section class="card card--back" aria-label="Postcard back">
  <svg class="curve" width="551" height="390" viewBox="0 0 551 390" aria-hidden="true">
    <path d="M0 264 L300 264 L300 390 L0 390 Z" fill="#e6e7e6"/>
    <path d="M262 0 L305 0 C318 110 300 150 287 240 C280 300 280 350 283 390 L268 390 C258 320 262 260 273 200 C286 130 290 70 262 0 Z" fill="#ffffff"/>
    <path d="M263 0 L301 0 C314 90 298 150 286 225 C279 280 278 340 283 390 L277 390 C266 330 266 270 276 205 C288 130 290 60 263 0 Z" fill="#00953a"/>
    <path d="M259 0 L264 0 C285 70 284 135 271 205 C260 265 262 330 271 390 L267 390 C256 325 255 265 266 205 C279 135 279 70 259 0 Z" fill="#b7dc78"/>
  </svg>

  <h1 class="headline back-headline">
    <span class="light">Getting cash is easy</span>
    <span class="dark">at Ridgeline Title Loans</span>
  </h1>

  <p class="about">Ridgeline Title Loans knows that every customer has different needs. We promise that no one else will work as hard as we do to earn and keep your business. As a trusted lender since 1995, we pride ourselves on providing critical funds to hard-working people who may simply need a little help from time to time. Our friendly and qualified loan counselors take the time to understand your circumstances and will work hard to find loans that are right for your needs. We offer several types of fast cash loans so that our customers can get exactly what they need.</p>

  <h2 class="back-contact-title">CONTACT US</h2>
  <div class="back-contact-rule"></div>
  <div class="contact-line contact-line--phone">
    <svg width="12" height="10" viewBox="0 0 12 10" aria-hidden="true"><path d="M1 3 C1 1 3 1 6 1 C9 1 11 1 11 3 L9 4 L8 3 L4 3 L3 4 Z M3 5 L9 5 L10 9 L2 9 Z" fill="#b7dc78"/></svg>
    123-456-789
  </div>
  <div class="contact-line contact-line--web">
    <svg width="10" height="10" viewBox="0 0 10 10" aria-hidden="true"><circle cx="5" cy="5" r="4.5" fill="#b7dc78"/><path d="M0.5 5 H9.5 M5 0.5 V9.5" stroke="#ffffff" stroke-width=".8"/></svg>
    www.ridgelinegroup.com
  </div>
  <div class="social">
    <span class="lead">Get in touch with us</span>
    <span class="dot"></span><span class="dot"></span><span class="dot"></span>
  </div>

  <div class="stamp-box" aria-label="Postage stamp area"></div>
</section>

<div class="side-label side-label--front">front</div>
<div class="side-label side-label--back">Back</div>

</body>
</html>
```